Bluefinch Painting needs a Website

We need a website built for a Painting company I own, we mainly do residential painting, but don't want to be limited to that.

Need to have estimate request form.
Need pic's of past projects

I like the look of the website for http://www.harborline-painters.example
& "Wexley Property inspections"

My logo that was designed here on ArtHive on the front page

I would like one of the houses I downloaded as part of the background
of the front page.

Target Market(s)

Home owners

Industry/Entity Type

Painting

Number of Pages Required

1 page

Font styles to use
Serif

Requirements
Must have
• Estimate request form for home owners to fill out -
• Name:
• Phone Number:
• Address:
• E-mail:
• Painting project description:
• And my info to:
• My phone number: (555) 318-7046
• My web address bluefinchpainting.example
Nice to have
• My logo that was designed here on ArtHive

```html
<!DOCTYPE html>
<html lang="en">
<head>
<meta charset="utf-8">
<title>Bluefinch Painting</title>
<link rel="stylesheet" href="https://fonts.googleapis.com/css2?family=Bebas+Neue&family=Dosis:wght@400;500;600;700&display=swap">
<style>
:root{
  --blue:#1f78c1;
  --blue-dark:#17609e;
  --ink:#2b2b2b;
  --grey:#777;
  --line:#d9d9d9;
  --field:#ececec;
  --footer:#262324;
  --white:#fff;
  --card-repair:#c49484;
  --card-design:#6c6940;
  --card-interior:#d7cbb6;
  --card-exterior:#f4b43a;
}
*{box-sizing:border-box;margin:0;padding:0}
html,body{width:1200px;height:3172px;overflow:hidden;background:var(--white)}
body{position:relative;font-family:"Dosis",sans-serif;color:var(--ink)}
.abs{position:absolute}

/* header */
.social{top:24px;left:850px;display:flex;gap:10px}
.social span{width:36px;height:36px;border-radius:50%;background:var(--blue)}
.social span:nth-child(4){background:#345}
.phone{top:86px;left:872px;display:flex;align-items:center;gap:10px;font-size:19px;color:#444}
.brand{top:86px;left:0;width:1200px;display:flex;justify-content:center;align-items:center;gap:16px}
.brand-mark{width:44px;height:44px;background:var(--blue)}
.brand-name{font-family:"Dosis",sans-serif;font-weight:600;font-size:42px;color:var(--blue);letter-spacing:1px}
.nav{top:227px;left:124px;width:906px;border-top:2px solid var(--line);display:flex;justify-content:space-between;align-items:center;padding-top:10px}
.nav a{font-size:18px;color:#444;text-decoration:none;text-transform:uppercase}
.nav a.active{color:var(--blue)}
.nav i{width:7px;height:7px;border-radius:50%;background:var(--blue)}

/* hero */
.hero{top:270px;left:0;width:1200px;height:576px;background:linear-gradient(180deg,#7d8f9a 0%,#5c6a5f 45%,#3e4f33 100%)}
.hero-copy{top:455px;left:0;width:1200px;text-align:center;color:var(--white)}
.hero-copy h1{font-family:"Bebas Neue",sans-serif;font-weight:400;font-size:74px;letter-spacing:3px;line-height:1}
.hero-copy p{font-size:22px;margin-top:6px}
.hero-btn{top:595px;left:481px;width:217px;height:47px;border:1px solid var(--blue);color:var(--blue);font-size:20px;display:flex;align-items:center;justify-content:center;text-transform:uppercase;background:rgba(0,0,0,.25)}
.arrow{top:536px;width:46px;height:46px;border-radius:50%;background:var(--blue);display:flex;align-items:center;justify-content:center}
.dots{display:flex;gap:6px}
.dots i{width:10px;height:10px;border-radius:50%;background:#ccc}
.dots i:first-child{background:var(--blue)}

/* category band */
.band{top:846px;left:0;width:1200px;height:69px;background:var(--blue);display:flex;align-items:center;justify-content:center;gap:64px;color:var(--white);font-size:22px;letter-spacing:1px}
.band i{width:7px;height:7px;border-radius:50%;background:var(--white)}

.heading{left:0;width:1200px;text-align:center;font-family:"Bebas Neue",sans-serif;font-size:44px;color:var(--blue);letter-spacing:2px;font-weight:400}
.about-text{top:1010px;left:185px;width:833px;text-align:center;font-size:13px;line-height:1.55;color:var(--grey)}

/* services */
.services-shadow{top:1212px;left:0;width:1200px;height:14px;background:linear-gradient(180deg,rgba(0,0,0,.12),rgba(0,0,0,0))}
.services{top:1224px;left:166px;width:867px;height:380px;display:flex}
.card{flex:1;position:relative;color:var(--white);padding:20px 16px}
.card.repair{background:linear-gradient(160deg,#d8a898,var(--card-repair))}
.card.design{background:linear-gradient(160deg,#7c7948,var(--card-design))}
.card.interior{background:linear-gradient(160deg,#e6dccb,var(--card-interior))}
.card.exterior{background:linear-gradient(160deg,#f7c55c,var(--card-exterior))}
.card .num{font-size:44px;opacity:.55;line-height:1}
.card h3{font-weight:400;font-size:43px;line-height:1.1;margin-top:54px;text-transform:uppercase}
.card p{font-size:13px;line-height:1.4;margin-top:10px}
.card .more{position:absolute;right:16px;bottom:14px;font-size:11px;display:flex;align-items:center;gap:4px}

/* testimonial */
.avatar{top:1723px;left:481px;width:238px;height:238px;border-radius:50%;background:radial-gradient(circle at 50% 40%,#e9d3bf,#b98f6f 60%,#6d5a4c)}
.client-name{top:1980px;left:0;width:1200px;text-align:center;font-size:26px;color:#333}
.quote{top:2028px;left:270px;width:660px;text-align:center;font-size:14px;line-height:1.5;color:#aaa}
.quote-mark{top:2000px;left:238px;font-size:56px;color:var(--blue);font-family:Georgia,serif}

/* eco banner */
.eco{top:2157px;left:0;width:1200px;height:269px;background:linear-gradient(90deg,#6e3a48 0%,#3d5a2e 30%,#2b2f2b 50%,#3d5a2e 70%,#7a3d4c 100%)}
.eco-copy{top:2198px;left:0;width:1200px;text-align:center;color:var(--white);line-height:1.1}
.eco-copy .big{font-size:56px;font-weight:500}
.eco-copy .sub{font-size:36px;font-weight:500}
.eco-btn{top:2360px;left:537px;width:179px;height:45px;background:var(--blue);color:var(--white);font-size:20px;font-weight:600;display:flex;align-items:center;justify-content:center}

/* quote form */
.form{top:2548px;left:156px;width:854px}
.fields{display:flex;gap:16px}
.fields span,.desc{background:var(--field);border:1px solid #d5d5d5;color:#999;font-size:14px;padding:5px 8px}
.fields span{flex:1;height:29px}
.desc{margin-top:11px;height:214px}
.submit{margin-top:8px;height:37px;background:var(--blue);color:var(--white);font-size:20px;display:flex;align-items:center;justify-content:center}

/* footer */
.footer{top:2881px;left:0;width:1200px;height:291px;background:var(--footer);color:var(--white)}
.fcol{top:58px}
.fcol h4{font-weight:500;font-size:20px;text-transform:uppercase}
.fcol h4.cap{text-transform:none}
.fcol a{display:block;color:#ccc;font-size:14px;margin-top:16px;text-decoration:none;text-transform:uppercase}
.contact-row{display:flex;align-items:center;gap:12px;color:#ccc;font-size:14px;margin-top:18px}
.fsocial{display:flex;gap:6px;margin-top:14px}
.fsocial span{width:20px;height:20px;border-radius:50%;background:var(--blue)}
.truck{top:159px;left:782px;width:222px;height:118px;background:linear-gradient(180deg,#3a3838,#e8e8e8 45%,#bdbdbd 80%,#3a3838)}
.copy{bottom:12px;left:0;width:1200px;text-align:center;font-size:13px;color:#888}
</style>
</head>
<body>

<header>
  <div class="abs social"><span></span><span></span><span></span><span></span></div>
  <div class="abs phone">
    <svg width="22" height="22" viewBox="0 0 24 24"><path d="M6.6 10.8a15 15 0 0 0 6.6 6.6l2.2-2.2c.3-.3.7-.4 1-.2 1.1.4 2.3.6 3.6.6.6 0 1 .4 1 1V20c0 .6-.4 1-1 1A17 17 0 0 1 3 4c0-.6.4-1 1-1h3.5c.6 0 1 .4 1 1 0 1.3.2 2.5.6 3.6.1.3 0 .7-.2 1z" fill="none" stroke="#555" stroke-width="1.6"/></svg>
    (555) 318-7046
  </div>
  <div class="abs brand"><span class="brand-mark"></span><span class="brand-name">Bluefinch Painting</span></div>
  <nav class="abs nav">
    <a class="active">Home</a><i></i><a>About Us</a><i></i><a>Services</a><i></i><a>Gallery</a><i></i><a>Contact</a>
  </nav>
</header>

<section>
  <div class="abs hero" role="img" aria-label="Photo of a two-storey house with garden and the company van in the driveway"></div>
  <div class="abs hero-copy"><h1>Where Dreams Meet Reality</h1><p>The best home painters are yours for the taking.</p></div>
  <div class="abs hero-btn">Contact Now</div>
  <div class="abs arrow" style="left:40px"><svg width="14" height="14" viewBox="0 0 14 14"><path d="M9 2 4 7l5 5" fill="none" stroke="#fff" stroke-width="2"/></svg></div>
  <div class="abs arrow" style="left:1114px"><svg width="14" height="14" viewBox="0 0 14 14"><path d="m5 2 5 5-5 5" fill="none" stroke="#fff" stroke-width="2"/></svg></div>
  <div class="abs dots" style="top:780px;left:554px"><i></i><i></i><i></i><i></i></div>
</section>

<div class="abs band"><span>EXTERIOR</span><i></i><span>INTERIOR</span><i></i><span>RESIDENTIAL</span><i></i><span>COMMERCIAL</span></div>

<section>
  <h2 class="abs heading" style="top:945px">About Us</h2>
  <p class="abs about-text">We are a family-run painting team serving home owners across the region. From a single accent wall to a full exterior refresh, we prepare every surface with care, use durable low-odor paints and keep your home clean while we work. Every project starts with a free estimate and ends with a walkthrough, so you know exactly what you are paying for and love the finished result.</p>
</section>

<section>
  <h2 class="abs heading" style="top:1146px">Our Services</h2>
  <div class="abs services-shadow"></div>
  <div class="abs services">
    <article class="card repair" role="img" aria-label="Photo of wall repair work">
      <div class="num">01</div><h3>Repair Services</h3>
      <p>No matter what the project you can always bet there will be repairs needed. We fix cracks, rot and dents before any paint goes on, with no hidden extra charges.</p>
      <span class="more">VIEW MORE &rarr;</span>
    </article>
    <article class="card design" role="img" aria-label="Photo of a designed interior room">
      <div class="num">02</div><h3>Interior Design</h3>
      <p>People think painting is the hard part of the job. Choosing colors from hundreds of shades can be overwhelming, and we are here to guide you.</p>
      <span class="more">VIEW MORE &rarr;</span>
    </article>
    <article class="card interior" role="img" aria-label="Photo of a freshly painted interior">
      <div class="num">03</div><h3>Interior Painting</h3>
      <p>Sometimes all a room needs is a fresh coat of paint. Walls, ceilings and trim are finished with clean lines and no mess left behind.</p>
      <span class="more">VIEW MORE &rarr;</span>
    </article>
    <article class="card exterior" role="img" aria-label="Photo of a painted house exterior">
      <div class="num">04</div><h3>Exterior Painting</h3>
      <p>When it comes to painting your home exterior, we have all the tools and crew to make any outside project look new.</p>
      <span class="more">VIEW MORE &rarr;</span>
    </article>
  </div>
</section>

<section>
  <h2 class="abs heading" style="top:1662px">Our Clients Say</h2>
  <div class="abs avatar" role="img" aria-label="Portrait photo of a smiling client"></div>
  <div class="abs client-name">Lena Marsh</div>
  <div class="abs quote-mark">&ldquo;</div>
  <p class="abs quote">Bluefinch repainted our whole house in under a week. The crew was friendly, careful with our garden and the colors look even better than we imagined. We will call them again.</p>
  <div class="abs dots" style="top:2102px;left:554px"><i></i><i></i><i></i><i></i></div>
</section>

<section>
  <div class="abs eco" role="img" aria-label="Photo of a front door framed by flowering pink shrubs"></div>
  <div class="abs eco-copy"><div class="big">100%</div><div class="sub">Quality &amp; Eco-friendly</div><div class="sub">Materials</div></div>
  <div class="abs eco-btn">CALL US TODAY</div>
</section>

<section>
  <h2 class="abs heading" style="top:2468px">Request a Quote</h2>
  <form class="abs form">
    <div class="fields"><span>Name</span><span>Phone Number</span><span>Address</span><span>E-mail</span></div>
    <div class="desc">Description</div>
    <div class="submit">SUBMIT</div>
  </form>
</section>

<footer class="abs footer">
  <div class="abs fcol" style="left:140px"><h4>Home</h4><a>About Us</a><a>Services</a><a>Gallery</a><a>Contact</a></div>
  <div class="abs fcol" style="left:304px"><h4>Services</h4><a>Commercial</a><a>Residential</a><a>Interior</a></div>
  <div class="abs fcol" style="left:484px"><h4>Contact</h4>
    <div class="contact-row"><svg width="16" height="20" viewBox="0 0 16 20"><path d="M8 0a7 7 0 0 0-7 7c0 5 7 13 7 13s7-8 7-13a7 7 0 0 0-7-7zm0 10a3 3 0 1 1 0-6 3 3 0 0 1 0 6z" fill="#fff"/></svg>bluefinchpainting.example</div>
    <div class="contact-row"><svg width="16" height="16" viewBox="0 0 24 24"><path d="M6.6 10.8a15 15 0 0 0 6.6 6.6l2.2-2.2c.3-.3.7-.4 1-.2 1.1.4 2.3.6 3.6.6.6 0 1 .4 1 1V20c0 .6-.4 1-1 1A17 17 0 0 1 3 4c0-.6.4-1 1-1h3.5c.6 0 1 .4 1 1 0 1.3.2 2.5.6 3.6.1.3 0 .7-.2 1z" fill="none" stroke="#fff" stroke-width="1.8"/></svg>(555) 318-7046</div>
    <div class="contact-row"><svg width="16" height="12" viewBox="0 0 16 12"><rect x="0" y="0" width="16" height="12" fill="#fff"/><path d="M0 0l8 6 8-6" fill="none" stroke="#262324" stroke-width="1.3"/></svg>info@bluefinchpainting.example</div>
  </div>
  <div class="abs fcol" style="left:790px"><h4 class="cap">FOLLOW US</h4><div class="fsocial"><span></span><span></span><span></span><span></span><span></span></div></div>
  <div class="abs truck" role="img" aria-label="Photo of the company pickup truck with ladders"></div>
  <div class="abs copy">Copyright©2015 Bluefinch Painting. All rights reserved</div>
</footer>

</body>
</html>
```